Iconic Cool Labels for Amazing Coffee

I'm back again after a very successful logo design project, now looking for label designs!

NOTEs:

IF YOU SUBMIT A DESIGN YOU WILL DEFINITELY RECEIVE FEEDBACK. I think it's rude not to respond when somebody takes the time to devote their time and talent to a project like this.

THIS BRIEF IS LONG. Out of respect for you, the designers. I've put a lot of time into this to give you as much understanding as I can. I think if you are going to invest your time it is only right and proper that I do the same. So please don't be put off by the length - it is intended to save you time and energy.

THE BRIEF

We are launching a coffee website called Brewvantia aimed at those who really care about coffee and have a passion for getting the very best out of it. So far, we have a great logo (attached), we have the website under construction and with the look and feel decided.

We are not a mass market player - instead we are more like an online boutique. But, we are starting out and need to look chic in a way that doesn't involve large investments. So, our coffee will be packaged in bags (1kg and 250g) with brown paper exteriors (brown kraft) onto which we'll put self adhesive labels.This is where we need your help.

THE TASK
- Create the 2 "master" labels for the front of the bags
- Create the variety labels that go either on or somewhere around the master label
- Create a small label for the back of the bag that contains the required regulatory information

There are 2 "families" - each requiring a family label. They are our blends (there are 7 of these), our single origin coffees (there are 3 of these) and the fair trade organic.

MASTER LABELS - In my mind the main focus of this brief
For the front of the bag there will be a master label for each of the 2 families, with another self-adhesive label placed either on top of the master label or adjacent to it. The exception being the free trade organic - there is only one of these, so no over labelling required.

The master labels are the main game here. They need to be distinctive and tasteful. They should look "chic" but not "try hard". They should be different to each other yet clearly part of the same house.

Both master labels MUST include the Brewvantia logo (supplied) and must also include a small Tornaso logo somewhere. Tornaso is our roaster. Perhaps it might be "Proudly roasted by (Tornaso logo)", or something like that.

The master labels are needed in each of the 1kg and 250g sizes and should have the size displayed as a part of the label.

The 2 master labels are:
Blends - these are beans from multiple origins and are typically used for espresso, late etc. I'd prefer that the label doesn't say "blends".

Single Origin - these are coffees from a single place in the world. They are for enthusiasts who want to explore the nuance and subtlety of a single region. Rather than be made in an espresso machine (although they can be) siphons are where these truly come in to their own.

VARIETY LABEL
These will either be stuck in a designated space on the MASTER LABEL or will be stuck somewhere else on the usable area. There are 7 of these in the blends family and 3 in the single origins family. They may be all very similar in look and feel or they may be variations within a theme. What do you think they should be?

You may decide to make them look similar of different. You might have groups - e.g. the first four, the free trade organics and the decafs. (Though if you do please don't do the cliched thing and make the decafs blue!)

Our Varieties are:
BLENDS
The Waypost
The Devotee
The Sybarite
The Revelist
Free Trade Organic
Swiss Decafeinated
Mexican Mountain Decafeinated

SINGLE ORIGIN
Ethiopian Limou
Costa Rica La Lapa
Nicaraguan Marigogipe Superior

COMPLIANCE LABEL
This is a small label to go onto the back of the bag for all of our coffees. It contains all of the regulatory and compliance information. I'd like this to be small and reasonably unobtrusive, but clearly from the same "stable" as the other labels. This should be a regular shape so it's easy and quick to stick on, but not necessarily a rectangle - you pick.

It should contain:

Brewvantia
PO Box 4736
Prahran VIC 3181
www.brewvantia.com.au

Roasted, Blended & Packed in Australia
from Imported Beans

Store away from sunlight in a cool dry place

TECHNICAL DETAILS
The usable areas are (in portrait format)
1kg - 180mm high by 100mm wide
250g - 140mm high by 70mm wide

How much of this space you use and how you use it is up to you. My ingoing feeling is that using all of the available space would make it look "mass market" rather than premium. On the front, maybe there are a couple of small labels that are spaced, maybe there's one big label with an over sticker. I don't want to constrain you too much in this regard - except to say that unusual shapes like stars may be both slow and awkward to put onto the bags

THE CREATIVE SIDE
This is where you come in...
- Do you use all the space of just some of it (my guess is the latter)?
- One master on the front with an oversticker for variety or 2 separate labels?
- Rectangular labels or another shape (not jagged shapes please - too hard to stick evenly)
- Does the label contain, just words or does it have images, photos etc?
- Are the variety labels all similar or do they have a different look and feel?

ATTACHMENTS
- Brewvantia logo pack in zip file
- Tornaso logo
- Some photos I shared for the logo brief as examples
Updates

All, 

The files I thought I'd attached didn't get there the first time. I think I've corrected that now. Sorry for any hassle caused.

Cheers,
Gus

Target Market(s)

Our target customers have one thing in common - they are passionate about excellent coffee. While they come from all walks of life the image in my head is of young professionals that wear designer clothes - lots of black - and are passionate about design. They aspire to have Lurst furniture and care passionately about both design and functionality. They go to the cinema, but mainly arthouse and foreign. They visit the theatre and art galleries. They care about their coffee and the making of it might even be described as a ritual. They have separate grinders and espresso machines and are especially particular about everything to do with coffee - the beans (where they come from and how they are roasted), the grind, the making of the coffee itself, right down to the cups and glasses in which they are served.

Industry/Entity Type

Construction

Requirements
Must have
• A look and feel of premiumness without being staid. I think companies that have done this incredible well include Veltro, Sorna, Quell, Darui, KTR. They are clearly premium, but have a feeling of what I describe as understated cutting edge about them. There is a lot of work that has gone into all of their graphic material yet they don't look "try hard".The colour palate is quite narrow - black, white, silver/chrome, and various coffee shades ranging perhaps from the golden brown of the crema to the rich dark brown of a roasted bean.
Nice to have
• I would like the coffee bag to be something that people leave out because it looks cool an chic.
Should not have
• Please avoid the cliches. I was thrilled with the creativity in the logo work, so I am enthusiastic at the prospect of seeing the same here.

Importantly, please avoid steaming cups at all costs! Also, pictures of people sipping coffee and looking blissfully content are not what I'm looking for.

Also, out emphasis is italian style coffee - espresso, late etc rather than the long black coffee that comes out of a filter machine that is popular in the US - consequently images that connote that should be avoided.

```html
<!DOCTYPE html>
<html lang="en">
<head>
<meta charset="utf-8">
<title>Brewvantia – Bag Labels</title>
<link rel="stylesheet" href="https://fonts.googleapis.com/css2?family=Jost:wght@400;500&display=swap">
<style>
  :root {
    --page: #ffffff;
    --kraft: #c7a06a;
    --kraft-dark: #b88f58;
    --kraft-light: #d1ad78;
    --label-panel: #cfa972;
    --ink: #1b1511;
    --black: #0c0a09;
    --white: #f6f2ea;
    --marker: #222222;
  }
  * { margin: 0; padding: 0; box-sizing: border-box; }
  html, body {
    width: 1200px; height: 900px; overflow: hidden;
    background: var(--page);
    font-family: "Jost", "Futura", sans-serif;
  }
  .canvas { position: relative; width: 1200px; height: 900px; }

  .bag {
    position: absolute; top: 44px; width: 480px; height: 830px;
    background:
      repeating-linear-gradient(90deg, rgba(0,0,0,0.035) 0 1px, transparent 1px 4px),
      linear-gradient(160deg, var(--kraft-light), var(--kraft) 45%, var(--kraft-dark));
  }
  .bag--single { left: 44px; }
  .bag--blend { left: 676px; }

  /* master label */
  .master {
    position: absolute; left: 148px; top: 46px; width: 184px; height: 214px;
    background: rgba(255,255,255,0.06);
  }
  .master__head {
    position: absolute; left: 20px; top: 14px; width: 148px; height: 140px;
    background: var(--black);
    display: flex; flex-direction: column; align-items: center;
  }
  .master__mark {
    margin-top: 30px; width: 46px; height: 46px; border-radius: 50%;
    border: 2px solid var(--kraft-light);
  }
  .master__name {
    margin-top: 20px; color: var(--white); font-size: 13px; font-weight: 500;
    letter-spacing: 6px; text-transform: uppercase; padding-left: 6px;
  }
  .master__copy {
    position: absolute; left: 20px; top: 154px; width: 148px; height: 56px;
    background: var(--label-panel);
    padding: 7px 8px 0; color: var(--ink); font-size: 9.5px; line-height: 13px;
    text-align: justify;
  }
  .roaster { font-weight: 500; letter-spacing: 0.5px; }
  .size { float: right; }

  /* variety label */
  .variety {
    position: absolute; left: 104px; top: 416px; width: 272px; height: 370px;
    background: rgba(255,255,255,0.06);
  }
  .variety__frame {
    position: absolute; left: 6px; top: 6px; width: 260px; height: 298px;
    background: var(--black);
  }
  .variety__family, .variety__name {
    position: absolute; left: 0; width: 100%; text-align: center;
    color: var(--white); font-size: 15px; font-weight: 500;
    letter-spacing: 4px; text-transform: uppercase;
  }
  .variety__family { top: 10px; }
  .variety__name { top: 270px; }
  .variety__image {
    position: absolute; left: 6px; top: 38px; width: 248px; height: 224px;
  }
  .variety__image--chart {
    background: radial-gradient(ellipse at 40% 50%, #d8d6d0, #b9b7b1 70%, #a09e98);
  }
  .variety__image--tap {
    background: radial-gradient(ellipse at 55% 35%, #9c9c9a, #4a4a48 55%, #1e1e1d);
  }
  .variety__notes {
    position: absolute; left: 6px; top: 304px; width: 260px; height: 58px;
    background: var(--label-panel);
    padding: 8px 14px 0; color: var(--ink); font-size: 11px; line-height: 15px;
    text-align: justify;
  }

  .version {
    position: absolute; left: 578px; top: 404px;
    color: var(--marker); font-size: 20px; font-weight: 400;
  }
</style>
</head>
<body>
<main class="canvas">

  <section class="bag bag--single">
    <div class="master">
      <div class="master__head">
        <div class="master__mark"></div>
        <div class="master__name">Brewvantia</div>
      </div>
      <p class="master__copy">Hand selected varieties blended in unique and suprising combinations roasted in Australia by <span class="roaster">Tornaso</span> <span class="size">1kg</span></p>
    </div>
    <div class="variety">
      <div class="variety__frame">
        <h2 class="variety__family">Single Origin</h2>
        <div class="variety__image variety__image--chart" role="img" aria-label="Antique sea chart of a coastline in black and white"></div>
        <h3 class="variety__name">Ethiopian Limou</h3>
      </div>
      <p class="variety__notes">Exotic fruity citrus and delicate dark chocolate with a hint of spices</p>
    </div>
  </section>

  <div class="version">C2</div>

  <section class="bag bag--blend">
    <div class="master">
      <div class="master__head">
        <div class="master__mark"></div>
        <div class="master__name">Brewvantia</div>
      </div>
      <p class="master__copy">Hand selected varieties blended in unique and suprising combinations roasted in Australia by <span class="roaster">Tornaso</span> <span class="size">1kg</span></p>
    </div>
    <div class="variety">
      <div class="variety__frame">
        <h2 class="variety__family">Special Blend</h2>
        <div class="variety__image variety__image--tap" role="img" aria-label="Black and white photograph of an ornate vintage tap"></div>
        <h3 class="variety__name">The Waypost</h3>
      </div>
      <p class="variety__notes">Exotic fruity citrus and delicate dark chocolate with a hint of spices</p>
    </div>
  </section>

</main>
</body>
</html>
```